Performance and Functional Training for Life
Project: Business Card & Letterhead
Business Card & Letterhead
Bright & Fun-filled
Dale Varnek
Strength & Conditioning Coach
42 Millbrook Lane Brackett, MA 01958
dale@strideformlab.com
www.strideformlab.com
Whether competing on the field of play or in the game of life Stride Form Lab is your proven partner for: Performance Enhancement Injury Reduction & Rehabilitation Weight Management & Nutritional Strategies General Fitness Consulting to Companies and Schools Team Training

```html
<!DOCTYPE html>
<html lang="en">
<head>
<meta charset="utf-8">
<title>Stride Form Lab – Business Card</title>
<link href="https://fonts.googleapis.com/css2?family=Open+Sans:ital,wght@0,400;0,600;0,700;1,400;1,600&display=swap" rel="stylesheet">
<style>
  :root {
    --bg: #e9eaec;
    --blue-deep: #0b2f9e;
    --blue: #1446c8;
    --blue-light: #2f6ae6;
    --grey-band: #6d6f74;
    --ink: #4a4c52;
    --white: #ffffff;
  }
  * { margin: 0; padding: 0; box-sizing: border-box; }
  html, body { width: 1200px; height: 901px; overflow: hidden; background: var(--bg); }
  body { position: relative; font-family: "Open Sans", Arial, sans-serif; }

  .card {
    position: absolute;
    width: 700px; height: 400px;
    border-radius: 4px;
    overflow: hidden;
    box-shadow: 0 6px 18px rgba(0,0,0,0.18);
  }

  /* Back of card */
  .card-back {
    left: 60px; top: 40px;
    background: radial-gradient(ellipse at 40% 35%, var(--blue-light) 0%, var(--blue) 45%, var(--blue-deep) 100%);
    color: var(--white);
    text-align: center;
  }
  .back-brand {
    margin-top: 70px;
    display: flex; align-items: center; justify-content: center; gap: 10px;
    font-weight: 700; font-size: 22px;
  }
  .brand-dot { width: 16px; height: 16px; border-radius: 50%; background: var(--white); }
  .back-intro { margin-top: 28px; font-size: 15px; line-height: 1.45; }
  .service-list { list-style: none; margin-top: 18px; font-size: 15px; line-height: 1.45; }

  /* Front of card */
  .card-front { left: 440px; top: 461px; background: var(--white); }
  .front-swoosh { position: absolute; inset: 0; }
  .front-brand { position: absolute; left: 40px; top: 58px; }
  .brand-line { display: flex; align-items: center; gap: 10px; }
  .brand-line .brand-dot { background: var(--blue); width: 18px; height: 18px; }
  .brand-name { font-weight: 700; font-size: 30px; color: var(--blue-deep); letter-spacing: -0.5px; }
  .brand-tagline { margin-top: 2px; font-style: italic; font-weight: 600; font-size: 14px; color: var(--blue); }

  .person { position: absolute; right: 34px; top: 128px; text-align: right; color: var(--white); }
  .person-name { font-weight: 700; font-size: 17px; }
  .person-title { font-style: italic; font-size: 15px; }

  .address { position: absolute; left: 40px; top: 250px; font-style: italic; font-size: 15px; color: var(--ink); line-height: 1.35; }

  .contacts { position: absolute; right: 34px; bottom: 24px; list-style: none; font-size: 14px; color: var(--ink); }
  .contacts li { display: flex; align-items: center; gap: 10px; line-height: 1.65; }
  .contacts svg { width: 14px; height: 14px; fill: var(--blue); flex: none; }
</style>
</head>
<body>

<section class="card card-back" aria-label="Card back">
  <div class="back-brand"><span class="brand-dot"></span>Stride Form Lab</div>
  <p class="back-intro">Whether competing on the field of play or in the game of life<br>Stride Form Lab is your proven partner for:</p>
  <ul class="service-list">
    <li>Performance Enhancement</li>
    <li>Injury Reduction &amp; Rehabilitation</li>
    <li>Weight Management &amp; Nutritional Strategies</li>
    <li>General Fitness</li>
    <li>Consulting to Companies and Schools</li>
    <li>Team Training</li>
  </ul>
</section>

<section class="card card-front" aria-label="Card front">
  <svg class="front-swoosh" viewBox="0 0 700 400" preserveAspectRatio="none" aria-hidden="true">
    <defs>
      <linearGradient id="swooshBlue" x1="0" y1="0" x2="1" y2="1">
        <stop offset="0" stop-color="#2f6ae6"/>
        <stop offset="1" stop-color="#0b2f9e"/>
      </linearGradient>
    </defs>
    <path d="M322 0 Q460 250 700 284 V262 Q490 232 346 0 Z" fill="#6d6f74"/>
    <path d="M346 0 H700 V262 Q490 232 346 0 Z" fill="url(#swooshBlue)"/>
  </svg>

  <div class="front-brand">
    <div class="brand-line"><span class="brand-dot"></span><span class="brand-name">Stride Form Lab</span></div>
    <p class="brand-tagline">Performance and Functional Training for Life</p>
  </div>

  <div class="person">
    <p class="person-name">Dale Varnek</p>
    <p class="person-title">Strength &amp; Conditioning Coach</p>
  </div>

  <p class="address">42 Millbrook Lane<br>Brackett, MA 01958</p>

  <ul class="contacts">
    <li><svg viewBox="0 0 16 16"><path d="M3 1h3l1.5 4-2 1.2a9 9 0 0 0 4.3 4.3L11 8.5l4 1.5v3a2 2 0 0 1-2 2A13 13 0 0 1 1 3a2 2 0 0 1 2-2z"/></svg>781-555-0142</li>
    <li><svg viewBox="0 0 16 16"><path d="M1 3h14v10H1z M1 3l7 6 7-6" stroke="#fff" stroke-width="1.2"/></svg>dale@strideformlab.com</li>
    <li><svg viewBox="0 0 16 16"><circle cx="8" cy="8" r="7"/><path d="M1 8h14M8 1c3 3 3 11 0 14M8 1c-3 3-3 11 0 14" stroke="#fff" stroke-width="1" fill="none"/></svg>www.strideformlab.com</li>
  </ul>
</section>

</body>
</html>
```